business card with 2 locations on 1 card

I need a modern looking business card that I would use at 2 different locations. Possibly 1 location on 1 side and other location on other side. One should be able to distinguish the 2 locations immediately before having to read the address or description on card. You can take a look at my website to see what I'm drawn to. The logo is brand new that I just purchased on Pixel Harbor. I want to emphasize family.
Updates

Let's not use the yellow and blue colors. Added Thursday, August 31, 2017

Target Market(s)

women and children

Industry/Entity Type

Health And Wellness

Contact Information for Business Card

Business name: Willow Nest Chiropractic & Acupuncture
My name: Delsa Brook
Job title: DC, MAOM, LAc (CA), CNS

Location 1
Address: 4817 Marlowe Blvd, Suite C-200, Frisco, TX 75036
Phone: (469) 555-0182
Fax: (972) 555-0147

Location 2
Address: 1786 Tenley Road, Suite 300, Plano, TX 75079
Phone: (469) 555-0195
Fax: (972) 555-0147

Email: drdelsabrook@mailvex.example
Website: www.drdelsabrook.example

Font styles to use
Serif
Sans Serif

Colors

Designer to choose colors to be used in the design.

Requirements
Must have
• distinction between 2 locations.
Nice to have
• Colors preference below is there. But I like to see what you come up with too!

```html
<!DOCTYPE html>
<html lang="en">
<head>
<meta charset="utf-8">
<title>Willow Nest Chiropractic &amp; Acupuncture – Business Card</title>
<link href="https://fonts.googleapis.com/css2?family=Cinzel:wght@600&family=Arimo:wght@400;700&display=swap" rel="stylesheet">
<style>
  :root{
    --teal:#3f726b;
    --teal-dark:#35645d;
    --leaf:#3e8c2a;
    --lime:#a8e46c;
    --paper:#ffffff;
    --silver:#e3e5e4;
    --ink:#3a3a3a;
    --bg-top:#c9c9cb;
    --bg-bottom:#dcdcde;
  }
  *{box-sizing:border-box;margin:0;padding:0}
  html,body{width:1200px;height:990px;overflow:hidden}
  body{
    background:linear-gradient(180deg,var(--bg-top),var(--bg-bottom));
    font-family:"Arimo",Arial,sans-serif;
    position:relative;
  }
  .card{
    position:absolute;top:341px;width:540px;height:308px;
    border-radius:18px;overflow:hidden;
    box-shadow:0 4px 10px rgba(0,0,0,.22);
  }
  .card--front{left:40px;background:var(--paper)}
  .card--back{left:620px;background:var(--teal)}
  .card svg.shape{position:absolute;inset:0;width:100%;height:100%}

  .brand{position:absolute;text-align:center;color:var(--teal)}
  .brand__dot{
    display:block;margin:0 auto;border-radius:50%;
    border:4px solid var(--teal);
  }
  .brand__name{font-family:"Cinzel",Georgia,serif;font-weight:600;line-height:1.15}

  .card--front .brand{left:24px;width:230px;top:22px}
  .card--front .brand__dot{width:92px;height:92px}
  .card--front .brand__name{font-size:17px;margin-top:10px}

  .person{position:absolute;left:24px;width:230px;top:188px;text-align:center;color:var(--ink)}
  .person__name{color:var(--leaf);font-weight:700;font-size:17px;letter-spacing:.3px}
  .person__title{font-size:12.5px;margin-top:3px}
  .person__contact{font-size:12px;margin-top:18px;line-height:1.45}

  .office{position:absolute;right:34px;text-align:right;color:var(--paper);font-size:12px;line-height:1.45}
  .office--plano{top:30px}
  .office--frisco{top:174px}
  .office__label{color:var(--lime);font-weight:700;font-size:12.5px;display:flex;justify-content:flex-end;align-items:center;gap:6px}
  .office__label svg{width:7px;height:11px}
  .office__phones{margin-top:14px}

  .card--back .pattern{position:absolute;inset:0}
  .card--back .brand{left:0;right:0;top:62px;color:var(--paper)}
  .card--back .brand__dot{width:112px;height:112px;border-color:var(--paper);background:var(--teal-dark)}
  .card--back .brand__name{font-size:24px;margin-top:14px}
</style>
</head>
<body>

<section class="card card--front" aria-label="Business card front">
  <svg class="shape" viewBox="0 0 540 308" preserveAspectRatio="none" aria-hidden="true">
    <path d="M276,0 C262,90 246,200 258,308 L540,308 L540,0 Z" fill="var(--silver)"/>
    <path d="M288,0 C274,90 258,200 270,308 L540,308 L540,0 Z" fill="var(--leaf)"/>
    <path d="M302,0 C288,90 272,200 284,308 L540,308 L540,0 Z" fill="var(--teal)"/>
  </svg>

  <div class="brand">
    <span class="brand__dot"></span>
    <p class="brand__name">Willow Nest<br>Chiropractic &amp; Acupuncture</p>
  </div>

  <div class="person">
    <p class="person__name">DELSA BROOK</p>
    <p class="person__title">DC, MAOM, LAc (CA), CNS</p>
    <p class="person__contact">drdelsabrook@mailvex.example<br>www.drdelsabrook.example</p>
  </div>

  <div class="office office--plano">
    <p class="office__label">PLANO'S OFFICE: <svg viewBox="0 0 7 11"><path d="M7,0 L0,5.5 L7,11 Z" fill="var(--lime)"/></svg></p>
    <p>1786 Tenley Road, Suite 300<br>Plano, TX 75079</p>
    <p class="office__phones">Phone: (469) 555-0195<br>Fax: (972) 555-0147</p>
  </div>

  <div class="office office--frisco">
    <p class="office__label">FRISCO'S OFFICE: <svg viewBox="0 0 7 11"><path d="M7,0 L0,5.5 L7,11 Z" fill="var(--lime)"/></svg></p>
    <p>4817 Marlowe Blvd, Suite C-200<br>Frisco, TX 75036</p>
    <p class="office__phones">Phone: (469) 555-0182<br>Fax: (972) 555-0147</p>
  </div>
</section>

<section class="card card--back" aria-label="Business card back">
  <div class="pattern" role="img" aria-label="Soft pattern of faint leaves across the teal background"
       style="background:radial-gradient(ellipse at 50% 55%, #4a7d76 0%, var(--teal) 70%)"></div>
  <div class="brand">
    <span class="brand__dot"></span>
    <p class="brand__name">Willow Nest<br><span style="font-size:13px">Chiropractic &amp; Acupuncture</span></p>
  </div>
</section>

</body>
</html>
```